Luxury Brand Real Estate For Sale sign

**Update** I've added some examples from the internet of other signs that have a look similar to what I would like to see. I do not want my personal name in the sign. And the word FOR SALE Does not need to be so large - it can be more subtle.
I want to create a Real Estate for sale sign for my company that will be used for luxury/higher end real estate listings. I’m sharing my business card as well as a logo with new teal color to show what we're moving towards: we’re using Teal, white, black and gold.
Hoping the sign is simple, sophisticated and eye catching.
The sign should be 24" wide by 30" tall including the company name: Harbor Crest Realty Group and our logo, office phone number 727-555-0148 and website www.hcrgexample.com the words "For Sale"
Optional to add this e-mail address info@hcrgexample.com to the sign
Target Market(s)
Luxury home buyers
Industry/Entity Type
Real Estate
Look and feel

```html
<!DOCTYPE html>
<html lang="en">
<head>
<meta charset="utf-8">
<title>Harbor Crest Realty Group — For Sale Sign</title>
<link rel="stylesheet" href="https://fonts.googleapis.com/css2?family=Josefin+Sans:wght@300;400&family=Montserrat:wght@400;500&display=swap">
<style>
  :root {
    --charcoal: #343233;
    --sky: #29c3f0;
    --white: #ffffff;
    --backdrop: #f1f1ef;
  }
  * { margin: 0; padding: 0; box-sizing: border-box; }
  html, body {
    width: 1200px;
    height: 542px;
    overflow: hidden;
    background: var(--backdrop);
  }
  .canvas {
    position: relative;
    width: 1200px;
    height: 542px;
  }
  .sign {
    position: absolute;
    top: 124px;
    width: 256px;
    height: 324px;
    font-family: "Josefin Sans", sans-serif;
    box-shadow: 0 2px 6px rgba(0,0,0,0.12);
  }
  .sign--classic { left: 120px; }
  .sign--bright { left: 779px; }

  .sign__header {
    position: absolute;
    left: 0; top: 0;
    width: 100%;
    height: 83px;
    display: flex;
    align-items: center;
    justify-content: center;
    gap: 8px;
  }
  .brand__mark {
    width: 14px;
    height: 14px;
  }
  .brand__name {
    font-family: "Montserrat", sans-serif;
    font-weight: 500;
    font-size: 10.5px;
    line-height: 1.15;
    letter-spacing: 0.04em;
    text-transform: uppercase;
  }

  .sign__body {
    position: absolute;
    left: 0; top: 83px;
    width: 100%;
    height: 241px;
  }
  .headline {
    position: absolute;
    left: 0; top: 12px;
    width: 100%;
    text-align: center;
    font-weight: 400;
    font-size: 78px;
    line-height: 60px;
    letter-spacing: 0.01em;
  }
  .headline span { display: block; }
  .headline__rule {
    position: absolute;
    left: 60px; top: 135px;
    width: 136px;
    height: 2px;
  }
  .contact__phone {
    position: absolute;
    left: 0; top: 172px;
    width: 100%;
    text-align: center;
    font-weight: 300;
    font-size: 33px;
    letter-spacing: 0.01em;
    line-height: 1;
  }
  .contact__web {
    position: absolute;
    left: 0; top: 207px;
    width: 100%;
    text-align: center;
    font-family: "Montserrat", sans-serif;
    font-size: 7.6px;
    letter-spacing: 0.12em;
  }

  /* Classic colourway */
  .sign--classic .sign__header { background: var(--white); }
  .sign--classic .brand__mark { background: var(--charcoal); }
  .sign--classic .brand__name { color: var(--charcoal); }
  .sign--classic .sign__body { background: var(--charcoal); color: var(--white); }
  .sign--classic .headline__rule { background: var(--white); }

  /* Bright colourway */
  .sign--bright .sign__header { background: var(--charcoal); }
  .sign--bright .brand__mark { background: var(--sky); }
  .sign--bright .brand__name { color: var(--sky); }
  .sign--bright .sign__body { background: var(--sky); color: var(--charcoal); }
  .sign--bright .headline__rule { background: var(--charcoal); }
  .sign--bright .contact__phone { color: var(--white); }

  .divider {
    position: absolute;
    left: 598px; top: 178px;
    width: 4px;
    height: 186px;
    background: var(--charcoal);
  }
</style>
</head>
<body>
<main class="canvas">

  <section class="sign sign--classic">
    <header class="sign__header">
      <div class="brand__mark"></div>
      <div class="brand__name">Harbor Crest<br>Realty Group</div>
    </header>
    <div class="sign__body">
      <h1 class="headline"><span>FOR</span><span>SALE</span></h1>
      <div class="headline__rule"></div>
      <p class="contact__phone">727-555-0148</p>
      <p class="contact__web">www.hcrgexample.com | info@hcrgexample.com</p>
    </div>
  </section>

  <div class="divider"></div>

  <section class="sign sign--bright">
    <header class="sign__header">
      <div class="brand__mark"></div>
      <div class="brand__name">Harbor Crest<br>Realty Group</div>
    </header>
    <div class="sign__body">
      <h1 class="headline"><span>FOR</span><span>SALE</span></h1>
      <div class="headline__rule"></div>
      <p class="contact__phone">727-555-0148</p>
      <p class="contact__web">www.hcrgexample.com | info@hcrgexample.com</p>
    </div>
  </section>

</main>
</body>
</html>
```